tilebaron.org needs a cool website!

I need a website designed for a commercial flooring maintenance company based in Texas. We will be providing services like carpet shampooing, burnishing, resurfacing and power washing. It needs to be cool and trendy.

I’ll need 10-20 pages. I need help deciding on the style and color palette. We will need great stock pictures of different flooring types and you will need to photo shop our logo on imaginary cars or storefronts.

Please have similar experience and an open mind. I’m looking for a partnership and someone to turn to for future projects and upkeep.

The domain is currently hosted on Wix. You will need the ability to develop and code it there.
Updates

Target Market(s)

Commercial businesses and properties

Industry/Entity Type

Floor care

Coding

Coded - Design and coding required

Number of Pages Required

5+ page

Requirements
Must have
• Great pictures of different types of floors.

```html
<!DOCTYPE html>
<html lang="en">
<head>
<meta charset="utf-8">
<title>tilebaron — Expert Commercial Flooring Maintenance</title>
<link rel="stylesheet" href="https://fonts.googleapis.com/css2?family=Overpass:wght@400;600;700;800&display=swap">
<style>
  :root {
    --lime: #94d13a;
    --lime-button: #84c83a;
    --lime-dark: #6ea932;
    --ink: #1b1b1b;
    --white: #ffffff;
    --star: #f5c518;
    --hero-dark: #2a2f2c;
    --hero-mid: #4b5650;
    --hero-green: #3f5a3a;
  }
  * { box-sizing: border-box; margin: 0; padding: 0; }
  html, body {
    width: 1200px;
    height: 900px;
    overflow: hidden;
    background: var(--white);
    font-family: "Overpass", sans-serif;
    color: var(--ink);
  }
  .page { position: relative; width: 1200px; height: 900px; overflow: hidden; }

  /* Header */
  .site-header {
    position: absolute; top: 0; left: 0; width: 1200px; height: 86px;
    background: var(--white);
    display: flex; align-items: center;
  }
  .brand {
    position: absolute; left: 138px; top: 26px;
    display: flex; align-items: center; gap: 8px;
    font-size: 28px; font-weight: 400; color: var(--ink); letter-spacing: 0.5px;
  }
  .brand-dot { width: 12px; height: 12px; border-radius: 50%; background: var(--lime); }
  .main-nav {
    position: absolute; left: 452px; top: 31px;
    display: flex; gap: 25px;
    font-size: 19px; letter-spacing: 0.4px;
  }
  .call-button {
    position: absolute; left: 897px; top: 21px; width: 167px; height: 46px;
    border-radius: 8px; background: var(--lime-button); color: var(--white);
    display: flex; align-items: center; justify-content: center; gap: 6px;
    font-size: 17px; font-weight: 700; letter-spacing: 0.6px;
  }

  /* Hero */
  .hero { position: absolute; top: 86px; left: 0; width: 1200px; height: 650px; }
  .hero-photo {
    position: absolute; inset: 0;
    background:
      radial-gradient(ellipse at 85% 40%, rgba(63,90,58,0.85), transparent 55%),
      radial-gradient(ellipse at 10% 30%, rgba(70,95,60,0.7), transparent 45%),
      linear-gradient(180deg, var(--hero-mid) 0%, var(--hero-dark) 75%, #1e2220 100%);
  }
  .hero-content {
    position: absolute; top: 0; left: 0; width: 1200px;
    text-align: center; color: var(--white);
  }
  .hero-title {
    margin-top: 95px;
    font-size: 76px; font-weight: 700; line-height: 94px; letter-spacing: 1.5px;
  }
  .hero-rating {
    margin-top: 22px;
    display: flex; align-items: center; justify-content: center; gap: 14px;
  }
  .stars { display: flex; gap: 3px; }
  .hero-brand { font-size: 34px; font-weight: 400; color: var(--white); letter-spacing: 0.5px; }
  .hero-tagline {
    margin-top: 16px;
    font-size: 22px; font-weight: 700; color: var(--lime); letter-spacing: 0.4px;
  }
  .book-button {
    display: inline-flex; align-items: center; justify-content: center;
    margin-top: 40px; width: 188px; height: 51px; border-radius: 7px;
    background: var(--lime-button); color: var(--white);
    font-size: 19px; font-weight: 700; letter-spacing: 0.8px;
  }

  /* Service: burnishing */
  .service-burnishing { position: absolute; top: 690px; left: 0; width: 1200px; height: 260px; background: var(--lime); }
  .hero-wave { position: absolute; top: 640px; left: 0; }
  .service-card {
    position: absolute; left: 108px; top: 67px; width: 501px; height: 394px;
    border: 8px solid var(--white); border-radius: 14px;
    background: linear-gradient(160deg, #e9ebea 0%, #c9cfcc 45%, #9c7d5c 75%, #2f3f5f 100%);
  }
  .service-text { position: absolute; left: 713px; top: 62px; color: var(--white); }
  .service-title { font-size: 48px; font-weight: 700; line-height: 54px; letter-spacing: 0.8px; }
  .service-body { margin-top: 26px; font-size: 28px; line-height: 32px; letter-spacing: 0.6px; }
</style>
</head>
<body>
<div class="page">
  <header class="site-header">
    <div class="brand"><span class="brand-dot"></span>tilebaron</div>
    <nav class="main-nav">
      <span>About Us</span>
      <span>Our Services</span>
      <span>FAQ</span>
    </nav>
    <div class="call-button">
      <svg width="16" height="20" viewBox="0 0 16 20" aria-hidden="true">
        <path d="M4 1 L7 1 L8 6 L5.5 7.5 C6 11 8 14 10.5 15.5 L12.5 13.5 L15.5 16 L14 19 C7 19 2 11 2.5 3 Z" fill="#ffffff"/>
      </svg>
      CALL US
    </div>
  </header>

  <section class="hero">
    <div class="hero-photo" role="img" aria-label="Photo of cleaning crew in overalls vacuuming and mopping a polished office floor among planters"></div>
    <div class="hero-content">
      <h1 class="hero-title">Love your floor<br>a little more..</h1>
      <div class="hero-rating">
        <div class="stars" aria-label="Five star rating">
          <svg width="150" height="28" viewBox="0 0 150 28" aria-hidden="true">
            <g fill="#f5c518">
              <path id="star" d="M14 1 L17.5 10 L27 10.5 L19.5 16.5 L22 26 L14 20.5 L6 26 L8.5 16.5 L1 10.5 L10.5 10 Z"/>
              <use href="#star" x="31"/>
              <use href="#star" x="62"/>
              <use href="#star" x="93"/>
              <use href="#star" x="124"/>
            </g>
          </svg>
        </div>
        <span class="hero-brand">tilebaron</span>
      </div>
      <p class="hero-tagline">Expert Commercial Flooring Maintenance</p>
      <div class="book-button">BOOK NOW</div>
    </div>
  </section>

  <svg class="hero-wave" width="1200" height="110" viewBox="0 0 1200 110" aria-hidden="true">
    <path d="M0 55 C150 95 320 92 560 62 C800 30 1000 0 1200 35 L1200 110 L0 110 Z" fill="#94d13a"/>
  </svg>

  <section class="service-burnishing">
    <div class="service-card" role="img" aria-label="Photo of a worker running a blue floor burnishing machine in an open office"></div>
    <div class="service-text">
      <h2 class="service-title">We Offer<br>Floor Burnishing</h2>
      <p class="service-body">Burnishing services on all<br>commercial facilities and</p>
    </div>
  </section>
</div>
</body>
</html>
```